Interior Design Company - Project Folder Design

Require simple layout design for company folders in a specific template as attach. Company name is MOVALT. Tag line is "make our visions alive, lasting, timeless" in Microsoft Word <Juice ITC> font type. Corporate colors include dark grey, turqoise and white.
Logo, AI template and some images are attached.

Company focus on Interior Design and Build services. Our services includes all commercial and residential projects.

Target Market(s)

B2B,B2C Corporate and Residential Design, Fit-outs and Project Management

Industry/Entity Type

Interior

Font styles to use
Sans Serif

Colors
33a6d7
333333
ffffff

Requirements
Must have
• Logo
• Address - No. 58 Kerrow Lane #04-21, Danvel Centre, Singapore 177492
• Web - www.movalt.com
Nice to have
• Clean professional architectural lines
Should not have
• No cartoons, kiddy images nor repetitive patterns

```html
<!DOCTYPE html>
<html lang="en">
<head>
<meta charset="utf-8">
<title>MOVALT Project Folder</title>
<link rel="stylesheet" href="https://fonts.googleapis.com/css2?family=Josefin+Sans:wght@300;700&family=Tinos:ital@1&display=swap">
<style>
  :root {
    --stage-top: #0b3436;
    --stage-bottom: #020c0d;
    --panel: #4a4a4a;
    --panel-dark: #3b3b3b;
    --panel-edge: #2c2c2c;
    --ink: #ffffff;
    --ink-soft: #d8d8d8;
    --accent: #33a6d7;
    --line-tone: #5c5c5c;
  }
  * { margin: 0; padding: 0; box-sizing: border-box; }
  html, body { width: 1200px; height: 798px; overflow: hidden; }
  body {
    background: radial-gradient(ellipse at 50% 30%, var(--stage-top), var(--stage-bottom) 80%);
    font-family: "Josefin Sans", sans-serif;
  }
  .folder-dieline {
    position: absolute;
    left: 47px;
    top: 60px;
    width: 1106px;
    height: 679px;
  }
  .panel { fill: var(--panel); stroke: var(--panel-edge); stroke-width: 1; }
  .panel--flap { fill: var(--panel-dark); }
  .fold-strip { fill: var(--panel-dark); stroke: var(--panel-edge); stroke-width: 1; }
  .slot-cut { fill: none; stroke: #222; stroke-width: 1; }
  .line-field-a { fill: url(#lineFieldA); }
  .line-field-b { fill: url(#lineFieldB); }
  .brand-name { font-family: "Josefin Sans", sans-serif; font-weight: 300; fill: var(--ink); }
  .service-list { font-family: "Josefin Sans", sans-serif; font-weight: 300; font-size: 10px; fill: var(--ink-soft); }
  .quote { font-family: "Tinos", serif; font-style: italic; font-size: 16.5px; fill: var(--ink); }
  .address, .web { font-family: "Josefin Sans", sans-serif; font-weight: 300; fill: var(--ink-soft); }
  .partner-name { font-family: "Josefin Sans", sans-serif; font-weight: 700; font-size: 8px; fill: var(--ink); }
  .partner-mark { fill: var(--ink); }
  .badge { fill: none; stroke: var(--ink); stroke-width: 2; }
</style>
</head>
<body>
<svg class="folder-dieline" viewBox="0 0 790 485" xmlns="http://www.w3.org/2000/svg" aria-label="MOVALT folder, flat layout">
  <defs>
    <linearGradient id="lineFieldA" x1="0" y1="0" x2="1" y2="1">
      <stop offset="0" stop-color="#4f6f72" stop-opacity="0.55"/>
      <stop offset="1" stop-color="#555" stop-opacity="0.3"/>
    </linearGradient>
    <linearGradient id="lineFieldB" x1="0" y1="0" x2="1" y2="1">
      <stop offset="0" stop-color="#5a5a5a" stop-opacity="0.6"/>
      <stop offset="1" stop-color="#525252" stop-opacity="0.2"/>
    </linearGradient>
  </defs>

  <!-- pocket flap with tabs -->
  <g class="pocket-flap">
    <path class="panel panel--flap" d="M4 0 H151 V32 H4 Z"/>
    <path class="panel panel--flap" d="M4 452 H151 L147 485 H8 Z"/>
    <rect class="panel" x="0" y="20" width="155" height="444"/>
    <polygon class="line-field-b" role="img" aria-label="Architectural line bundle" points="0,225 40,190 155,175 155,260 60,270 0,320"/>
    <text class="brand-name" x="30" y="92" font-size="24">movalt</text>
    <text class="service-list" x="23" y="126">Design.Build.Deco</text>
    <text class="service-list" x="23" y="140">Turnkey</text>
    <text class="service-list" x="23" y="154">Commercial</text>
    <text class="service-list" x="23" y="168">Residential</text>
    <text class="service-list" x="23" y="182">Customized Carpentry</text>
    <path class="slot-cut" d="M18 372 Q8 387 18 402"/>
    <path class="slot-cut" d="M92 372 Q80 387 90 402"/>
    <path class="slot-cut" d="M132 372 Q122 387 132 402"/>
    <path class="slot-cut" d="M50 428 Q75 408 100 428"/>
  </g>

  <rect class="fold-strip" x="155" y="32" width="5" height="420"/>

  <!-- inside back panel -->
  <g class="back-panel">
    <rect class="panel" x="160" y="32" width="308" height="420"/>
    <polygon class="line-field-a" role="img" aria-label="Turquoise architectural line bundle" points="160,90 220,70 300,70 330,32 400,32 330,110 250,120 190,180 160,180"/>
    <polygon class="line-field-b" role="img" aria-label="Grey architectural line bundle" points="160,180 190,180 250,120 330,110 400,32 468,32 360,150 260,170 200,230 160,230"/>
    <text class="quote" x="187" y="288">"Interior design is an extension</text>
    <text class="quote" x="191" y="306">of your personality coupled with</text>
    <text class="quote" x="187" y="324">life's experience."</text>
    <text class="address" x="224" y="424" font-size="12">No. 58 Kerrow Lane #04-21,</text>
    <text class="address" x="224" y="442" font-size="12">Danvel Centre, Singapore 177492</text>
  </g>

  <rect class="fold-strip" x="468" y="32" width="14" height="420"/>

  <!-- front cover -->
  <g class="front-cover">
    <rect class="panel" x="482" y="32" width="308" height="420"/>
    <polygon class="line-field-a" role="img" aria-label="Architectural line bundle" points="482,32 560,32 620,140 482,230"/>
    <polygon class="line-field-b" role="img" aria-label="Grey architectural line bundle" points="700,32 790,32 790,452 560,452"/>
    <text class="brand-name" x="610" y="103" font-size="24">movalt</text>
    <rect class="partner-mark" x="497" y="425" width="11" height="11"/>
    <text class="partner-name" x="512" y="429">CORVAN</text>
    <text class="partner-name" x="512" y="438">PAINT</text>
    <text class="web" x="597" y="437" font-size="11">www.movalt.com</text>
    <circle class="badge" role="img" aria-label="Partner award badge" cx="745" cy="419" r="23"/>
  </g>
</svg>
</body>
</html>
```